Business Cards for IT Consulting Company (Managed Service Provider)

I am looking to have some business cards printed and would like some designs. We are an IT Consulting company based in Vancouver BC. I would like a nice clean and modern look to the cards. I have uploaded all the versions of my logo so parts can be used as needed. Here is a snippit from our website homepage:

Kelbrook Systems Ltd. is an IT Solutions Partner located in Vancouver BC, Canada. We offer IT solutions and support to customers in the greater Vancouver Area. With expertise in Microsoft platforms, as well as Linux and Mac OSX and over 12 years experience in the IT industry, Kelbrook Systems is dedicated to offering our clients top quality service and products. We take pride in the solutions we offer our customers. The greatest compliment a client can give us is to recommend our services.

Kelbrook Systems Ltd. offers a wide range of IT services from onsite service to remote support and managed service solutions. This allows clients to choose the support path that best suits their company’s needs. Supporting many different sized companies from small to enterprise level over the past 12 years Kelbrook Systems has the experience and expertise needed to ensure things run smoothly. Allowing our clients to focus on doing business.

Revolutionizing the way IT services are delivered.

Kelbrook Systems is dedicated to providing our clients with IT solutions that work and grow with them for years to come. This philosophy helps save money in the long run instead of replacing equipment constantly. Far too often IT solutions are not well thought out and while possibly solving the problem at hand, require replacement due to growth or quality within a very short time frame. Kelbrook Systems takes pride in providing solutions that will last and be able to accommodate growth without the need for replacement.

Industry/Entity Type

Information Technology

Contact Information for Business Card

Kelbrook Systems Ltd.
(Employee Name)
Eml: (Employees Email Address)
Web: kelbrook.me
Ph: 604-555-0142

Font styles to use
Serif
Sans Serif

Requirements
Must have
• The Company logo and company colors.
Nice to have
• - Our tag line: "Revolutionizing IT Services" or "Revolutionizing the way IT services are delivered."
• - Also I really like the idea of nature and technology together blending which is sort of where my logo came from so integrating that somehow onto the business cards would be great.

```html
<!DOCTYPE html>
<html lang="en">
<head>
<meta charset="utf-8">
<title>Kelbrook Systems Ltd. — Business Card</title>
<link rel="stylesheet" href="https://fonts.googleapis.com/css2?family=Montserrat:wght@600&family=Open+Sans:wght@400;600&display=swap">
<style>
  :root {
    --backdrop: #6f6256;
    --card: #8b7e71;
    --card-edge: #b8ada2;
    --band-dark: #2c2724;
    --band-mid: #4a4440;
    --brand-blue: #3a7ca5;
    --ink-dark: #2a2a2a;
    --ink-light: #e4ddd6;
    --muted: #cfc6bd;
    --teal: #2f7f80;
  }
  html, body {
    margin: 0;
    width: 1200px;
    height: 1200px;
    overflow: hidden;
    background: var(--backdrop);
  }
  .card {
    position: absolute;
    left: 100px;
    top: 318px;
    width: 1000px;
    height: 565px;
    background: linear-gradient(160deg, #94887b 0%, var(--card) 55%, #7e7266 100%);
    border: 2px solid var(--card-edge);
    box-sizing: border-box;
    overflow: hidden;
    font-family: "Open Sans", Arial, sans-serif;
  }
  .card-shapes {
    position: absolute;
    inset: 0;
  }
  .pattern-area {
    position: absolute;
    right: 0;
    top: 0;
    width: 540px;
    height: 565px;
    background: radial-gradient(ellipse at 70% 50%, rgba(47,127,128,0.45) 0%, rgba(47,127,128,0.18) 45%, rgba(47,127,128,0) 75%);
  }
  .brand-name {
    position: absolute;
    left: 44px;
    top: 34px;
    margin: 0;
    font-family: "Montserrat", Arial, sans-serif;
    font-weight: 600;
    color: var(--brand-blue);
    line-height: 1;
  }
  .brand-name .brand-main {
    display: block;
    font-size: 66px;
    letter-spacing: 0.5px;
  }
  .brand-name .brand-sub {
    display: block;
    font-size: 24px;
    letter-spacing: 1px;
    margin-top: 6px;
  }
  .person {
    position: absolute;
    left: 81px;
    top: 303px;
  }
  .person-name {
    margin: 0;
    font-size: 32px;
    font-weight: 600;
    color: var(--brand-blue);
    line-height: 1.1;
  }
  .person-role {
    margin: 4px 0 0;
    font-size: 22px;
    color: var(--muted);
  }
  .contact-list {
    position: absolute;
    left: 50px;
    top: 416px;
    margin: 0;
    padding: 0;
    list-style: none;
  }
  .contact-item {
    display: flex;
    align-items: center;
    height: 34px;
    font-size: 22px;
    color: var(--ink-light);
  }
  .contact-icon {
    width: 18px;
    height: 18px;
    margin-right: 14px;
    flex: none;
  }
</style>
</head>
<body>
  <section class="card" aria-label="Kelbrook Systems business card">
    <svg class="card-shapes" width="1000" height="565" viewBox="0 0 1000 565" aria-hidden="true">
      <defs>
        <linearGradient id="band-gradient" x1="0" y1="0" x2="1" y2="0">
          <stop offset="0" stop-color="var(--band-dark)" stop-opacity="0.75"/>
          <stop offset="0.55" stop-color="var(--band-mid)" stop-opacity="0.85"/>
          <stop offset="1" stop-color="var(--band-dark)" stop-opacity="0.95"/>
        </linearGradient>
      </defs>
      <polygon class="contact-band" points="0,278 446,278 535,428 785,565 0,565" fill="url(#band-gradient)"/>
    </svg>

    <div class="pattern-area" role="img" aria-label="Teal hexagon outline pattern"></div>

    <h1 class="brand-name">
      <span class="brand-main">Kelbrook</span>
      <span class="brand-sub">SYSTEMS LTD.</span>
    </h1>

    <div class="person">
      <p class="person-name">Lena Hart</p>
      <p class="person-role">Managing Partner</p>
    </div>

    <ul class="contact-list">
      <li class="contact-item">
        <svg class="contact-icon" viewBox="0 0 18 18" aria-hidden="true">
          <path d="M4 2 L7 2 L8 6 L6 7.5 Q7.5 10.5 10.5 12 L12 10 L16 11 L16 14 Q16 16 14 16 Q3 15 2 4 Q2 2 4 2 Z" fill="var(--brand-blue)"/>
        </svg>
        <span>604-555-0142</span>
      </li>
      <li class="contact-item">
        <svg class="contact-icon" viewBox="0 0 18 18" aria-hidden="true">
          <rect x="1.5" y="4" width="15" height="10" rx="1.5" fill="var(--brand-blue)"/>
          <path d="M2 5 L9 10 L16 5" fill="none" stroke="var(--band-dark)" stroke-width="1.3"/>
        </svg>
        <span>lhart@kelbrook.me</span>
      </li>
      <li class="contact-item">
        <svg class="contact-icon" viewBox="0 0 18 18" aria-hidden="true">
          <circle cx="9" cy="9" r="7" fill="none" stroke="var(--brand-blue)" stroke-width="1.6"/>
          <ellipse cx="9" cy="9" rx="3" ry="7" fill="none" stroke="var(--brand-blue)" stroke-width="1.3"/>
          <line x1="2" y1="9" x2="16" y2="9" stroke="var(--brand-blue)" stroke-width="1.3"/>
        </svg>
        <span>kelbrook.me</span>
      </li>
    </ul>
  </section>
</body>
</html>
```